Pagevoより「最前線・空腹がすっと静まる献立&噛み方の手引き」というタイトルの電子書籍を出版予定です。

この本のコンセプトは「食べ物を選んで食べること&その食べ方で食欲が自然におさまること、更にはそれがダイエットと健康維持とアンチエイジングに非常に効果的であること、プラス今流行りのダイエット方(オートファジーダイエット、ミトコンドリア活性化、ケトジェニックダイエット、16時間断食、レクチンフリー 食品の勧め、腸活、SATエクササイズ、オイルの種類など)の説明とご提案(やり方)」をお伝えし、読者の皆様の健康維持に貢献したいということです。

ターゲットは男女ともに考えております。デザインは明るくて「何これ、ダイエットや食品の本にしては発想が新しい!」と興味を持ってもらえることを期待しております。(抽象的ですみません;)

何かご質問・ご提案がありましたらいつでもご連絡ください。
どうぞ宜しくお願いいたします。
*以下2項目の追加記載をお願いいたします。お手数ですがどうぞ宜しくお願いいたします。

・読者プレゼント
星座タイプ別 きみに向く減量術と献立チェック

・著者名: 森川 結奈
皆様、お忙しいところをたくさんのご応募、ありがとうございました!
どれも素敵なデザインでなかなか決めるのが難しいところではありますが、
数日中に決定、上位3名の方にご連絡いたします。

それでは、どうぞしばらくお待ちくださいませ。

取り急ぎ、お礼まで。

Thank you so much!
森川 結奈

当選:miru72_studio様 ー 明るくてフレッシュで清潔感のあるイメージで、何だろう?と書店だったら思わず手に取りたくなる素敵なデザインだと思いました。 次点:ripple_308様 ー デザインが可愛いく親しみやすいのと「食事を抑えるのでなく食欲を抑えるダイエット」など刺さるコピーがとても鋭いと感じました。執筆仲間にも好評でした。 次点: Hnbrook様 ー シンプルで見やすいが故に、逆に何が書いてあるんだろう?と興味を持たせてくれそうなデザインだと感じました。仲間内でも好評でした。

選定が遅くなり大変申し訳ございませんでした。この度は沢山の素敵なデザインをご提案くださり、ありがとうございました。 周りの者と相談の上、悩んだ末に決定させていただきました。 本当に素晴らしい作品ばかりで、デザインをするお仕事の素晴らしさを教えていただきました。 皆様のパワーにインスパイアされ、また二冊目も書きたいと思う原動力をいただきました。 またぜひご縁をいただけたら幸いです。 心より感謝申し上げます。どうもありがとうございました。 皆様のますますのご活躍とご発展をお祈り申し上げます。森川結奈

```html
<!DOCTYPE html>
<html lang="ja">
<head>
<meta charset="utf-8">
<title>最前線・空腹がすっと静まる献立&噛み方の手引き</title>
<link rel="stylesheet" href="https://fonts.googleapis.com/css2?family=M+PLUS+Rounded+1c:wght@500;800&family=Noto+Sans+JP:wght@500;700&display=swap">
<style>
:root{
  --frame:#f5c6cf;
  --paper:#fdf6d9;
  --pink:#e8507f;
  --pink-dark:#d93c6c;
  --brown:#553626;
  --ink:#3f302a;
  --orange:#f08a1c;
  --yellow:#f8d822;
  --figure-a:#f6b9c4;
  --figure-b:#f9dcc4;
}
*{margin:0;padding:0;box-sizing:border-box}
html,body{width:750px;height:1200px;overflow:hidden;background:var(--frame)}
.cover{position:relative;width:750px;height:1200px;background:var(--frame);font-family:"Noto Sans JP",sans-serif;color:var(--ink);overflow:hidden}
.cover__paper{position:absolute;inset:18px;background:var(--paper);border-radius:10px;overflow:hidden}
.badge-row{position:absolute;top:34px;left:0;right:0;display:flex;justify-content:center;gap:6px}
.badge-row__dot{width:42px;height:42px;border-radius:50%;background:var(--pink);color:#fff;font:800 24px/42px "M PLUS Rounded 1c",sans-serif;text-align:center}
.tagline{position:absolute;top:86px;left:0;right:0;text-align:center;font:700 46px/1 "Noto Sans JP",sans-serif;color:var(--ink);letter-spacing:2px}
.tagline-rule{position:absolute;top:146px;left:70px;right:70px;height:3px;background:var(--pink)}
.title{position:absolute;display:flex;flex-direction:column;align-items:center;font-family:"M PLUS Rounded 1c",sans-serif;font-weight:800}
.title__char{display:block;line-height:1}
.title--menu{left:490px;top:200px;font-size:156px;color:var(--pink)}
.title--chew{left:250px;top:200px;font-size:156px;color:var(--pink)}
.title--guide{left:56px;top:196px;font-size:128px;color:var(--brown)}
.title--menu .title__char,.title--chew .title__char{height:166px}
.title--guide .title__char{height:132px}
.title-amp{position:absolute;left:412px;top:330px;font:800 104px/1 "M PLUS Rounded 1c",sans-serif;color:var(--orange)}
.figure{position:absolute;left:220px;top:660px;width:380px;height:522px;border-radius:50% 50% 0 0/34% 34% 0 0;background:linear-gradient(180deg,var(--figure-b),var(--figure-a))}
.gift{position:absolute;left:36px;top:920px;width:212px;height:212px;border-radius:50%;background:var(--yellow);display:flex;flex-direction:column;align-items:center;justify-content:center;text-align:center;padding:0 18px}
.gift__label{font:700 24px/1.25 "Noto Sans JP",sans-serif;color:var(--pink-dark)}
.gift__text{margin-top:10px;font:500 16px/1.35 "Noto Sans JP",sans-serif;color:var(--ink)}
.author{position:absolute;right:90px;top:1120px;display:flex;align-items:baseline;gap:18px;color:var(--ink)}
.author__role{font:700 28px/1 "Noto Sans JP",sans-serif}
.author__name{font:700 46px/1 "Noto Sans JP",sans-serif;letter-spacing:4px}
</style>
</head>
<body>
<main class="cover">
  <div class="cover__paper"></div>

  <div class="badge-row" aria-label="最前線">
    <span class="badge-row__dot">最</span>
    <span class="badge-row__dot">前</span>
    <span class="badge-row__dot">線</span>
  </div>
  <p class="tagline">空腹がすっと静まる</p>
  <div class="tagline-rule"></div>

  <div class="figure" role="img" aria-label="フォークとナイフを両手に持ち笑顔で食事を待つ女性のイラスト"></div>

  <h1 aria-label="献立&amp;噛み方の手引き">
    <span class="title title--menu" aria-hidden="true"><span class="title__char">献</span><span class="title__char">立</span></span>
    <span class="title-amp" aria-hidden="true">&amp;</span>
    <span class="title title--chew" aria-hidden="true"><span class="title__char">噛</span><span class="title__char">み</span><span class="title__char">方</span></span>
    <span class="title title--guide" aria-hidden="true"><span class="title__char">の</span><span class="title__char">手</span><span class="title__char">引</span><span class="title__char">き</span></span>
  </h1>

  <div class="gift">
    <p class="gift__label">読者<br>プレゼント</p>
    <p class="gift__text">星座タイプ別<br>きみに向く減量術<br>と献立チェック</p>
  </div>

  <p class="author"><span class="author__role">著者</span><span class="author__name">森川 結奈</span></p>
</main>
</body>
</html>
```